Gourmet cookie company needs a label designed

We need a label designed for a new cookie company. We make mini cookies. The labels will be placed on either white tins or clear containers. We would like some bright and eye catching label although not child like. Our target customer is adults not kids.
Any color/colors acceptable. The initial label will be a square 4" label but the design should also be able to be formatted to fit on a round label as well in the future.

Text on label: Henrietta's Little Oven Company; Chocolate Chip; All Natural; New Wt. 8.0oz

```html
<!DOCTYPE html>
<html lang="en">
<head>
<meta charset="utf-8">
<title>Gourmet Cookie Company – Label Concepts</title>
<link rel="stylesheet" href="https://fonts.googleapis.com/css2?family=Parisienne&family=Cormorant+Garamond:ital,wght@1,500;1,600&family=Cormorant+Upright:wght@500;600&display=swap">
<style>
  :root {
    --board-bg: #fdf9f6;
    --frame-teal: #a3dbd3;
    --badge-teal: #8fd1c7;
    --badge-fill: #fcf5f1;
    --stripe-pink: #ec4a85;
    --stripe-light: #f8b9cf;
    --ink: #2e2a2a;
    --cookie-light: #e9c48f;
    --cookie-dark: #8a6a4c;
    --plate: #f0dbe8;
  }
  * { box-sizing: border-box; }
  html, body {
    margin: 0;
    width: 1200px;
    height: 848px;
    overflow: hidden;
    background: #ffffff;
  }
  .board {
    position: relative;
    width: 1200px;
    height: 848px;
    background: #ffffff;
  }
  .board__frame {
    position: absolute;
    left: 32px;
    top: 26px;
    width: 1146px;
    height: 798px;
    background: var(--board-bg);
    border: 9px solid var(--frame-teal);
    border-radius: 3px;
  }
  .board__title {
    position: absolute;
    left: 50px;
    top: 42px;
    margin: 0;
    font-family: "Parisienne", cursive;
    font-weight: 400;
    font-size: 42px;
    color: var(--frame-teal);
    letter-spacing: 0.5px;
  }
  .label {
    position: absolute;
    width: 410px;
    height: 410px;
    overflow: hidden;
    background: repeating-linear-gradient(
      90deg,
      var(--stripe-pink) 0 9px,
      var(--stripe-light) 9px 16px
    );
  }
  .label--square { left: 181px; top: 211px; }
  .label--round  { left: 631px; top: 207px; border-radius: 50%; }
  .label__badge {
    position: absolute;
    left: 40px;
    top: 57px;
    width: 330px;
    height: 303px;
  }
  .label__artwork {
    position: absolute;
    left: 110px;
    top: 95px;
    width: 190px;
    height: 140px;
    border-radius: 40% 40% 50% 50% / 30% 30% 20% 20%;
    background: radial-gradient(ellipse at 50% 45%, var(--cookie-light) 0%, var(--cookie-dark) 55%, var(--plate) 80%, transparent 100%);
  }
  .label__text {
    position: absolute;
    left: 0;
    right: 0;
    top: 256px;
    text-align: center;
    color: var(--ink);
    line-height: 20px;
  }
  .label__company {
    font-family: "Cormorant Garamond", serif;
    font-style: italic;
    font-weight: 600;
    font-size: 19px;
  }
  .label__detail {
    font-family: "Cormorant Upright", serif;
    font-weight: 600;
    font-size: 18px;
  }
</style>
</head>
<body>
<main class="board">
  <div class="board__frame"></div>
  <h1 class="board__title">Gourmet Cookie Company</h1>

  <section class="label label--square" aria-label="Square label">
    <svg class="label__badge" viewBox="0 0 330 303" aria-hidden="true">
      <path d="M70,14 Q165,0 260,14 Q266,40 292,46 Q318,52 318,78 Q330,150 318,225 Q318,251 292,257 Q266,263 260,289 Q165,303 70,289 Q64,263 38,257 Q12,251 12,225 Q0,150 12,78 Q12,52 38,46 Q64,40 70,14 Z"
            fill="var(--badge-fill)" stroke="var(--badge-teal)" stroke-width="10"/>
      <path transform="translate(165 151.5) scale(0.9) translate(-165 -151.5)"
            d="M70,14 Q165,0 260,14 Q266,40 292,46 Q318,52 318,78 Q330,150 318,225 Q318,251 292,257 Q266,263 260,289 Q165,303 70,289 Q64,263 38,257 Q12,251 12,225 Q0,150 12,78 Q12,52 38,46 Q64,40 70,14 Z"
            fill="none" stroke="var(--badge-teal)" stroke-width="1.2" stroke-dasharray="4 3"/>
    </svg>
    <div class="label__artwork" role="img" aria-label="Illustration of a stack of chocolate chip cookies on a pale pink plate"></div>
    <div class="label__text">
      <div class="label__company">Henrietta's Little Oven Company</div>
      <div class="label__detail">Chocolate Chip</div>
      <div class="label__detail">All Natural</div>
      <div class="label__detail">New Wt. 8.0 oz</div>
    </div>
  </section>

  <section class="label label--round" aria-label="Round label">
    <svg class="label__badge" viewBox="0 0 330 303" aria-hidden="true">
      <path d="M70,14 Q165,0 260,14 Q266,40 292,46 Q318,52 318,78 Q330,150 318,225 Q318,251 292,257 Q266,263 260,289 Q165,303 70,289 Q64,263 38,257 Q12,251 12,225 Q0,150 12,78 Q12,52 38,46 Q64,40 70,14 Z"
            fill="var(--badge-fill)" stroke="var(--badge-teal)" stroke-width="10"/>
      <path transform="translate(165 151.5) scale(0.9) translate(-165 -151.5)"
            d="M70,14 Q165,0 260,14 Q266,40 292,46 Q318,52 318,78 Q330,150 318,225 Q318,251 292,257 Q266,263 260,289 Q165,303 70,289 Q64,263 38,257 Q12,251 12,225 Q0,150 12,78 Q12,52 38,46 Q64,40 70,14 Z"
            fill="none" stroke="var(--badge-teal)" stroke-width="1.2" stroke-dasharray="4 3"/>
    </svg>
    <div class="label__artwork" role="img" aria-label="Illustration of a stack of chocolate chip cookies on a pale pink plate"></div>
    <div class="label__text">
      <div class="label__company">Henrietta's Little Oven Company</div>
      <div class="label__detail">Chocolate Chip</div>
      <div class="label__detail">All Natural</div>
      <div class="label__detail">New Wt. 8.0 oz</div>
    </div>
  </section>
</main>
</body>
</html>
```